Website - Corla Bastwick

I need a website that has multiple pages and easy for me to update pictures, content and blogs as an ongoing basis’s.
It will have videos and needs to be compatible to view easily and aesthetically on mobile phones.
Please refer to this website for inspiration www.velquistorin.com

Coding

Coded - Design and coding required

Number of Pages Required

5+ page

Font styles to use
Other font styles liked:
• Refer to website provided as inspiration

Requirements
Must have
• Please use stock images for now to do design, but I will be providing all imagery, videos and content

```html
<!DOCTYPE html>
<html lang="en">
<head>
<meta charset="utf-8">
<title>Corla Bastwick</title>
<link href="https://fonts.googleapis.com/css2?family=Raleway:wght@300;400;500;600;700&family=Lato:wght@400;700&display=swap" rel="stylesheet">
<style>
:root{
  --coral:#f64c58;
  --ink:#1f1f24;
  --muted:#77777f;
  --soft:#f7f7fc;
  --line:#dcdce2;
  --white:#ffffff;
}
*{margin:0;padding:0;box-sizing:border-box}
html,body{width:760px;height:1200px;overflow:hidden;background:var(--white)}
body{position:relative;font-family:'Raleway',sans-serif;color:var(--ink)}
.abs{position:absolute}
.hero{left:0;top:0;width:760px;height:425px;background:linear-gradient(180deg,#8e9e94 0%,#4f9791 22%,#5aa7a0 45%,#9a9a88 72%,#b9a58f 100%)}
.hero-shade{left:0;top:0;width:760px;height:425px;background:radial-gradient(ellipse at 50% 40%,rgba(120,90,70,.35),rgba(0,0,0,0) 55%),linear-gradient(180deg,rgba(0,0,0,.08),rgba(0,0,0,.18))}
.logo{left:74px;top:17px;font-size:21px;font-weight:400;color:var(--white);letter-spacing:.5px}
.nav a{position:absolute;top:23px;font-size:11px;color:var(--white);text-decoration:none;font-weight:400;white-space:nowrap}
.nav .pill{left:376px;top:20px;width:61px;height:21px;border:1px solid rgba(255,255,255,.9);border-radius:11px;text-align:center;line-height:19px}
.hero-arrow{width:25px;height:25px;border:1px solid rgba(255,255,255,.85);border-radius:50%;top:202px}
.hero-title{left:0;width:760px;text-align:center;color:var(--white)}
.t1{top:200px;font-size:30px;font-weight:700;letter-spacing:-1px}
.t2{top:240px;font-size:30px;font-weight:400;letter-spacing:-1px}
.t3{top:289px;font-size:9px;font-weight:400;letter-spacing:.2px}
.btn-videos{left:332px;top:323px;width:96px;height:20px;border-radius:10px;background:var(--coral);color:var(--white);font-size:7px;font-weight:600;letter-spacing:1px;text-align:center;line-height:20px}
.posts-title{left:109px;top:460px;font-size:27px;font-weight:300;color:var(--ink)}
.posts-title b{font-weight:700}
.search{left:497px;top:468px;width:154px;height:22px;background:#e1e1e4;border-radius:3px;font-size:9px;color:#55555c;padding-left:12px;line-height:22px}
.rule{height:1px;background:var(--line)}
.card{top:533px;width:171px;height:187px;background:var(--soft)}
.card .img{width:171px;height:126px}
.card h3{position:absolute;left:12px;top:140px;font-size:10px;font-weight:500;color:var(--ink)}
.card .meta{position:absolute;top:165px;font-size:8px;color:var(--muted);font-family:'Lato',sans-serif}
.card.active{box-shadow:0 6px 12px rgba(0,0,0,.12)}
.card.active h3{color:var(--coral)}
.play{position:absolute;left:73px;top:50px;width:26px;height:26px;border-radius:50%;background:rgba(40,40,40,.6)}
.red-arrow{width:23px;height:23px;border-radius:50%;background:var(--coral);top:591px}
.follow-gap{left:330px;top:776px;width:100px;height:16px;background:var(--white)}
.follow{left:0;width:760px;top:778px;text-align:center;font-size:9px;font-weight:600;font-family:'Lato',sans-serif}
.tile{top:807px;width:89px;height:89px}
.footer{left:0;top:930px;width:760px;height:227px;background:var(--soft)}
.top-btn{left:648px;top:941px;width:23px;height:23px;border-radius:50%;background:var(--coral)}
.top-label{left:636px;top:966px;width:47px;text-align:center;font-size:5.5px;font-family:'Lato',sans-serif}
.fh{top:995px;font-size:10px;font-weight:700;font-family:'Lato',sans-serif}
.ftext{font-size:7px;line-height:11.5px;color:#55555c;font-family:'Lato',sans-serif}
.qlinks a{display:block;font-size:6.5px;font-weight:700;color:#55555c;text-decoration:none;line-height:15.2px;font-family:'Lato',sans-serif}
.email{left:303px;top:1025px;width:132px;height:28px;border:1px solid #c9c6d6;background:var(--white);font-size:8.5px;color:var(--muted);padding-left:15px;line-height:26px}
.subscribe{left:303px;top:1058px;width:132px;height:29px;background:var(--coral);color:var(--white);font-size:8px;padding-left:12px;line-height:29px}
.thumb{width:30px;height:30px}
.rp{font-size:7.2px;line-height:10.5px;color:#44444c;font-family:'Lato',sans-serif}
.copy{left:0;width:760px;top:1170px;text-align:center;font-size:7.5px;color:#66666e}
</style>
</head>
<body>

<section class="hero abs" role="img" aria-label="Smiling woman in sunglasses by the sea"></section>
<div class="hero-shade abs"></div>

<div class="logo abs">Corla Bastwick</div>
<nav class="nav">
  <a class="pill" href="#">About</a>
  <a href="#" style="left:454px">Show Reels</a>
  <a href="#" style="left:534px">Tea With T</a>
  <a href="#" style="left:608px">Contact</a>
  <a href="#" style="left:662px">Picturegram</a>
</nav>

<div class="hero-arrow abs" style="left:77px"><svg width="23" height="23"><path d="M13 8.5 10 11.5 13 14.5" stroke="#fff" stroke-width="1.2" fill="none"/></svg></div>
<div class="hero-arrow abs" style="left:659px"><svg width="23" height="23"><path d="M10 8.5 13 11.5 10 14.5" stroke="#fff" stroke-width="1.2" fill="none"/></svg></div>

<h1 class="hero-title abs t1">Dummy Text</h1>
<p class="hero-title abs t2">to improve your business model</p>
<p class="hero-title abs t3">PARTICIPANTS AND SPEAKERS WELCOME</p>
<div class="btn-videos abs">OUR VIDEOS</div>
<svg class="abs" style="left:375px;top:395px" width="10" height="14"><rect x="1" y="1" width="8" height="12" rx="4" stroke="#fff" fill="none" stroke-width="1"/><line x1="5" y1="3.5" x2="5" y2="6" stroke="#fff"/></svg>

<h2 class="posts-title abs">Latest <b>Posts...</b></h2>
<div class="search abs">Search
  <svg class="abs" style="left:136px;top:8px" width="8" height="6"><path d="M1 1 4 4 7 1" stroke="#444" fill="none"/></svg>
</div>
<div class="rule abs" style="left:109px;top:507px;width:542px"></div>

<article class="card abs" style="left:109px">
  <div class="img" role="img" aria-label="Woman with curly hair in a checked jacket on a city street" style="background:linear-gradient(135deg,#6e7270,#2f3a33 60%,#a0643a)"></div>
  <div class="play"><svg width="26" height="26"><path d="M10 7 19 13 10 19Z" fill="var(--coral)"/></svg></div>
  <h3>Tea With T</h3>
  <span class="meta" style="left:12px">Admin</span><span class="meta" style="right:14px">2 Comments</span>
</article>
<article class="card abs active" style="left:295px">
  <div class="img" role="img" aria-label="Three people running into the sea on a beach" style="background:linear-gradient(180deg,#aeb2ad,#8f8b82 50%,#c9a07a)"></div>
  <div class="play"><svg width="26" height="26"><path d="M10 7 19 13 10 19Z" fill="var(--coral)"/></svg></div>
  <h3>Dance</h3>
  <span class="meta" style="left:12px">Admin</span><span class="meta" style="right:14px">2 Comments</span>
</article>
<article class="card abs" style="left:480px">
  <div class="img" role="img" aria-label="Two women laughing in front of a painted wall" style="background:linear-gradient(135deg,#c8c4c6,#b0787e 50%,#4d6f9a)"></div>
  <div class="play"><svg width="26" height="26"><path d="M10 7 19 13 10 19Z" fill="var(--coral)"/></svg></div>
  <h3>Act</h3>
  <span class="meta" style="left:12px">Admin</span><span class="meta" style="right:14px">2 Comments</span>
</article>
<div class="red-arrow abs" style="left:96px"><svg width="23" height="23"><path d="M12.5 9 10 11.5 12.5 14" stroke="#fff" stroke-width="1.3" fill="none"/></svg></div>
<div class="red-arrow abs" style="left:641px"><svg width="23" height="23"><path d="M10.5 9 13 11.5 10.5 14" stroke="#fff" stroke-width="1.3" fill="none"/></svg></div>

<div class="rule abs" style="left:109px;top:784px;width:542px"></div>
<div class="follow-gap abs"></div>
<p class="follow abs">Follow @ Picturegram</p>

<div class="tile abs" style="left:109px;background:linear-gradient(160deg,#d9c8b8,#8c6e5c)" role="img" aria-label="Hand holding a glass ball over a city skyline"></div>
<div class="tile abs" style="left:200px;background:linear-gradient(160deg,#a88f7c,#5d7fa8)" role="img" aria-label="Woman in sunglasses by a painted wall"></div>
<div class="tile abs" style="left:291px;background:linear-gradient(160deg,#f0c6c8,#c9a27c)" role="img" aria-label="Bearded man holding a dandelion"></div>
<div class="tile abs" style="left:382px;background:linear-gradient(160deg,#6a6660,#b8a89a)" role="img" aria-label="Woman in sunglasses leaning on a wall"></div>
<div class="tile abs" style="left:472px;background:linear-gradient(160deg,#d9c8b8,#8c6e5c)" role="img" aria-label="Hand holding a glass ball over a city skyline"></div>
<div class="tile abs" style="left:563px;background:linear-gradient(160deg,#e8e8ea,#9a5a35)" role="img" aria-label="Person in a cap and brown hoodie in snow"></div>

<footer class="footer abs"></footer>
<div class="top-btn abs"><svg width="23" height="23"><path d="M9 13 11.5 10.5 14 13" stroke="#fff" stroke-width="1.4" fill="none"/></svg></div>
<div class="top-label abs">Back to Top</div>

<h4 class="fh abs" style="left:102px">Our Address</h4>
<p class="ftext abs" style="left:102px;top:1022px;width:85px">48/ 9 number Orlen Address. 204/C Road 5B, Vantomere.</p>
<p class="ftext abs" style="left:102px;top:1067px">+55-031 7820 446<br>corlabastwick@mailvo.com</p>

<h4 class="fh abs" style="left:212px">Quick Links</h4>
<div class="qlinks abs" style="left:212px;top:1021px">
  <a href="#">Home</a><a href="#">About Us</a><a href="#">Show Reels</a><a href="#">Tea With T</a><a href="#">Contact Us</a>
</div>

<h4 class="fh abs" style="left:302px">Subscribe Now</h4>
<div class="email abs">Enter email Address</div>
<div class="subscribe abs">SUBSCRIBE NOW
  <svg class="abs" style="left:105px;top:10px" width="15" height="9"><path d="M0 4.5H13M9.5 1 13 4.5 9.5 8" stroke="#fff" fill="none"/></svg>
</div>

<h4 class="fh abs" style="left:476px">Recent Posts</h4>
<div class="thumb abs" style="left:476px;top:1021px;background:linear-gradient(#d8d4cc,#7c8a5a)" role="img" aria-label="Man holding leaves"></div>
<p class="rp abs" style="left:515px;top:1021px">Visiting Green<br>Field</p>
<div class="thumb abs" style="left:571px;top:1021px;background:linear-gradient(#6f7d5d,#3a3a30)" role="img" aria-label="Woman among green leaves"></div>
<p class="rp abs" style="left:610px;top:1021px">Simple Flower<br>Arements You<br>Can Put .</p>
<div class="thumb abs" style="left:476px;top:1067px;background:linear-gradient(#e4e4e6,#c59a3a)" role="img" aria-label="Person standing on a yellow vehicle"></div>
<p class="rp abs" style="left:515px;top:1068px">Europe's best<br>affordab</p>
<div class="thumb abs" style="left:572px;top:1066px;background:linear-gradient(#d8d4cc,#7c8a5a)" role="img" aria-label="Man holding leaves"></div>
<p class="rp abs" style="left:611px;top:1067px">Visiting Green<br>Field</p>

<p class="copy abs">Copyright © 2021 Corla Bastwick. All Rights Reserved.</p>

</body>
</html>
```